Corvane Real Estate Business Card

hello, we are a real estate company located in Los Angeles, california. we are a boutique, small company but we like a big corportate look. a simple, sleek, modern and progressive look. we would like the option of having a design that could include the real estate agents personal photo and also a design if the realtor desides not to have a photo. We also would like a hotizontal design.

Corvane Properties
3817 S Hadderly
West Hollywood, CA 90046
www.CorvaneRE.example

Gavin Prosk
Broker
BRE # 04829176
(555) 274-6390
gavin@corvanere.example

```html
<!DOCTYPE html>
<html lang="en">
<head>
<meta charset="utf-8">
<title>Corvane Real Estate – Business Card</title>
<link rel="stylesheet" href="https://fonts.googleapis.com/css2?family=Open+Sans:wght@400;500;600&display=swap">
<style>
  :root {
    --backdrop: #f1f1f0;
    --card-light: #e9e9e9;
    --brand-blue: #27598c;
    --name-blue: #2a5a8e;
    --ink: #1e1e1e;
    --icon-blue: #2a5a8e;
    --photo-top: #b9c4a6;
    --photo-mid: #7e8a70;
    --photo-low: #3a3d36;
    --white: #ffffff;
  }
  * { box-sizing: border-box; margin: 0; padding: 0; }
  html, body { width: 1200px; height: 800px; overflow: hidden; }
  body {
    background: var(--backdrop);
    font-family: "Open Sans", Arial, sans-serif;
    position: relative;
  }

  /* Front of card */
  .card-front {
    position: absolute;
    left: 120px; top: 348px;
    width: 570px; height: 320px;
    background: var(--card-light);
    box-shadow: 0 2px 6px rgba(0,0,0,0.12);
    overflow: hidden;
  }
  .brand-name {
    position: absolute;
    left: 34px; top: 32px;
    font-size: 30px;
    font-weight: 500;
    color: var(--name-blue);
    letter-spacing: -0.3px;
    line-height: 1;
  }
  .agent-name {
    position: absolute;
    left: 32px; top: 108px;
    font-size: 17px;
    color: var(--name-blue);
    line-height: 1.2;
  }
  .agent-title {
    position: absolute;
    left: 88px; top: 130px;
    font-size: 16px;
    color: var(--ink);
  }
  .license {
    position: absolute;
    left: 200px; top: 112px;
    font-size: 15px;
    color: var(--ink);
  }
  .contact-list {
    position: absolute;
    left: 28px; top: 176px;
    list-style: none;
    font-size: 15px;
    color: var(--ink);
  }
  .contact-item {
    display: flex;
    align-items: flex-start;
    line-height: 22px;
  }
  .contact-item + .contact-item { margin-top: 6px; }
  .contact-item.phone { margin-top: 3px; }
  .contact-item .icon {
    width: 20px; height: 22px;
    flex: none;
    margin-right: 15px;
  }
  .agent-photo {
    position: absolute;
    left: 350px; top: 0;
    width: 220px; height: 320px;
    background:
      radial-gradient(ellipse 60% 45% at 55% 40%, #d2a88c 0%, rgba(210,168,140,0) 70%),
      linear-gradient(180deg, var(--photo-top) 0%, var(--photo-mid) 45%, var(--photo-low) 100%);
  }

  /* Back of card */
  .card-back {
    position: absolute;
    left: 713px; top: 84px;
    width: 335px; height: 588px;
    background: var(--brand-blue);
    box-shadow: 0 2px 6px rgba(0,0,0,0.15);
    display: flex;
    align-items: center;
    justify-content: center;
  }
  .card-back .brand-mark {
    font-size: 36px;
    font-weight: 500;
    color: var(--white);
    letter-spacing: 0.5px;
  }
</style>
</head>
<body>

  <section class="card-front" aria-label="Business card front">
    <div class="brand-name">Corvane Properties</div>

    <div class="agent-name">Gavin Prosk</div>
    <div class="agent-title">Broker</div>
    <div class="license">BRE # 04829176</div>

    <ul class="contact-list">
      <li class="contact-item address">
        <svg class="icon" viewBox="0 0 20 22" aria-hidden="true">
          <path d="M10 2a5.5 5.5 0 0 0-5.5 5.5C4.5 12 10 19 10 19s5.5-7 5.5-11.5A5.5 5.5 0 0 0 10 2z" fill="var(--icon-blue)"/>
          <circle cx="10" cy="7.5" r="2" fill="var(--card-light)"/>
        </svg>
        <span>3817 S Hadderly<br>West Hollywood, CA 90046</span>
      </li>
      <li class="contact-item phone">
        <svg class="icon" viewBox="0 0 20 22" aria-hidden="true">
          <path d="M2 8c0-2 3-3.5 8-3.5S18 6 18 8v1.5h-4V8H6v1.5H2z" fill="var(--icon-blue)"/>
          <rect x="4" y="10" width="12" height="7" rx="1.5" fill="var(--icon-blue)"/>
          <circle cx="10" cy="13.5" r="2" fill="var(--card-light)"/>
        </svg>
        <span>(555) 274-6390</span>
      </li>
      <li class="contact-item email">
        <svg class="icon" viewBox="0 0 20 22" aria-hidden="true">
          <rect x="1" y="6" width="18" height="12" fill="var(--icon-blue)"/>
          <path d="M1.5 6.5 10 13l8.5-6.5" fill="none" stroke="var(--card-light)" stroke-width="1.4"/>
        </svg>
        <span>gavin@corvanere.example</span>
      </li>
      <li class="contact-item web">
        <svg class="icon" viewBox="0 0 20 22" aria-hidden="true">
          <circle cx="10" cy="11" r="8" fill="var(--icon-blue)"/>
          <path d="M2.5 11h15M10 3c-3 3-3 13 0 16M10 3c3 3 3 13 0 16M4 6.5h12M4 15.5h12" fill="none" stroke="var(--card-light)" stroke-width="1"/>
        </svg>
        <span>www.CorvaneRE.example</span>
      </li>
    </ul>

    <div class="agent-photo" role="img" aria-label="Portrait photo of the broker in a dark suit and tie"></div>
  </section>

  <section class="card-back" aria-label="Business card back">
    <div class="brand-mark">Corvane</div>
  </section>

</body>
</html>
```